Wedding Welcome Sign

Require a wedding welcome sign with wording as attached in picture
We are after something sophisticated, classy and elegant (simple and understated yet catchy)

Will be printed onto a mirror
Size of writing to cover 680mm high x 430mm wide

```html
<!DOCTYPE html>
<html lang="en">
<head>
<meta charset="utf-8">
<title>Wedding Welcome Sign</title>
<link href="https://fonts.googleapis.com/css2?family=Great+Vibes&display=swap" rel="stylesheet">
<style>
  :root {
    --sky-top: #6f8ea8;
    --sky-low: #c9d6df;
    --sea-deep: #2f7f86;
    --sea-shallow: #7cc6bd;
    --foam: #e6eee8;
    --sand-light: #f1d8a6;
    --sand: #ebcc92;
    --ink: #151515;
    --glow: rgba(64, 170, 160, 0.65);
    --ornament: #2a2320;
    --rule: #6b4a38;
  }
  * { margin: 0; padding: 0; box-sizing: border-box; }
  html, body {
    width: 675px;
    height: 1200px;
    overflow: hidden;
    background: var(--sand);
  }
  .sign {
    position: relative;
    width: 675px;
    height: 1200px;
    overflow: hidden;
    font-family: "Great Vibes", cursive;
    color: var(--ink);
  }
  .beach-scene {
    position: absolute;
    inset: 0;
    background: linear-gradient(
      to bottom,
      var(--sky-top) 0%,
      var(--sky-low) 7%,
      var(--sea-deep) 8%,
      var(--sea-shallow) 17%,
      var(--foam) 24%,
      var(--foam) 27%,
      var(--sand-light) 30%,
      var(--sand) 100%
    );
  }
  .ornament {
    position: absolute;
    left: 156px;
    width: 356px;
    height: 50px;
    background: var(--ornament);
    opacity: 0.85;
    border-radius: 25px;
  }
  .ornament--top { top: 152px; }
  .ornament--bottom { top: 1028px; }
  .line {
    position: absolute;
    left: 0;
    width: 100%;
    text-align: center;
    line-height: 1;
    white-space: nowrap;
    text-shadow: 2px 3px 4px var(--glow);
  }
  .vow { font-size: 60px; }
  .vow--1 { top: 232px; }
  .vow--2 { top: 304px; }
  .vow--3 { top: 375px; }
  .vow--4 { top: 446px; }
  .vow-love {
    top: 515px;
    font-size: 66px;
    font-weight: 700;
    -webkit-text-stroke: 1px var(--ink);
  }
  .vow-love span {
    text-decoration: underline;
    text-decoration-thickness: 3px;
    text-underline-offset: 6px;
  }
  .welcome { font-size: 96px; }
  .welcome--1 { top: 648px; }
  .welcome--2 { top: 748px; }
  .couple { top: 893px; font-size: 72px; }
  .date { top: 982px; font-size: 40px; }
  .base-rule {
    position: absolute;
    left: 31px;
    top: 1170px;
    width: 613px;
    height: 8px;
  }
</style>
</head>
<body>
<main class="sign">
  <div class="beach-scene" role="img" aria-label="Photograph of a tropical beach: cloudy sky and distant islands over turquoise sea, white surf washing onto golden sand"></div>

  <div class="ornament ornament--top" role="img" aria-label="Decorative scrolling floral flourish"></div>

  <p class="line vow vow--1">Today I marry my</p>
  <p class="line vow vow--2">best friend. The one</p>
  <p class="line vow vow--3">I laugh with, live for,</p>
  <p class="line vow vow--4">dream with,</p>
  <p class="line vow-love"><span>love.</span></p>

  <h1 class="line welcome welcome--1" style="font-weight:400">Welcome to</h1>
  <p class="line welcome welcome--2">our Wedding</p>

  <p class="line couple">Liam &amp; Clara</p>
  <p class="line date">20 May 2017</p>

  <div class="ornament ornament--bottom" role="img" aria-label="Decorative scrolling floral flourish"></div>

  <svg class="base-rule" viewBox="0 0 613 8" aria-hidden="true">
    <rect x="0" y="2" width="613" height="3" fill="#6fb7ad" opacity="0.6"/>
    <rect x="0" y="0" width="613" height="5" fill="var(--rule)"/>
  </svg>
</main>
</body>
</html>
```